KLT Business cards

I currently have a logo that was designed by a sketch harbor designer. I would like this to be added to the business card.

We are an innovative new start-up business offering finance solutions to the car dealership market in the UK. So our clients are quiet traditional, so are cards need to fit in, but at the same time show we are a modern online business.

Industry/Entity Type

Finance

```html
<!DOCTYPE html>
<html lang="en">
<head>
<meta charset="utf-8">
<title>KLT Business Cards</title>
<link rel="stylesheet" href="https://fonts.googleapis.com/css2?family=Arimo:wght@400;700&display=swap">
<style>
  :root {
    --navy: #142a4c;
    --white: #ffffff;
    --silver: #a9b6b8;
    --page: #ffffff;
    --shadow: rgba(0, 0, 0, 0.45);
  }
  * { box-sizing: border-box; margin: 0; padding: 0; }
  html, body {
    width: 1200px; height: 1000px; overflow: hidden;
    background: var(--page);
    font-family: "Arimo", Arial, sans-serif;
  }
  .card {
    position: absolute;
    width: 521px; height: 298px;
    box-shadow: 7px 7px 6px var(--shadow);
    overflow: hidden;
  }
  .card--front { left: 372px; top: 182px; background: var(--navy); }
  .card--back  { left: 370px; top: 542px; background: var(--white); }

  .brand { position: absolute; display: flex; align-items: center; }
  .brand__mark { flex: none; }
  .brand__name {
    font-weight: 400;
    line-height: 1.02;
  }
  .card--front .brand { left: 127px; top: 96px; }
  .card--front .brand__mark { width: 112px; height: 112px; margin-right: 12px; }
  .card--front .brand__name { color: var(--white); font-size: 31px; }

  .side-band {
    position: absolute; left: 57px; top: 0;
    width: 93px; height: 298px; background: var(--navy);
  }
  .card--back .brand { left: 56px; top: 18px; }
  .card--back .brand__mark { width: 98px; height: 98px; margin-right: 2px; }
  .card--back .brand__name { color: var(--navy); font-size: 22px; }

  .tagline {
    position: absolute; left: 66px; top: 188px;
    color: var(--white); font-weight: 700; font-size: 19px;
    line-height: 25px; letter-spacing: 0.3px;
  }
  .contact {
    position: absolute; right: 14px; top: 118px;
    text-align: right; color: var(--navy); font-weight: 700;
  }
  .contact__name { font-size: 17px; line-height: 22px; }
  .contact__role { font-size: 16px; line-height: 20px; color: var(--silver); margin-bottom: 21px; }
  .contact__line { font-size: 15px; line-height: 21px; }
  .contact__email { margin-top: 20px; }
</style>
</head>
<body>

<section class="card card--front">
  <div class="brand">
    <svg class="brand__mark" viewBox="0 0 112 112" aria-hidden="true">
      <circle cx="56" cy="56" r="50" fill="none" stroke="var(--white)" stroke-width="6"/>
    </svg>
    <p class="brand__name">Kestrel<br>Lane<br>Finance</p>
  </div>
</section>

<section class="card card--back">
  <div class="side-band"></div>
  <div class="brand">
    <svg class="brand__mark" viewBox="0 0 98 98" aria-hidden="true">
      <circle cx="49" cy="49" r="47" fill="var(--white)"/>
    </svg>
    <p class="brand__name">Kestrel<br>Lane<br>Finance</p>
  </div>
  <p class="tagline">DRIVE<br>NOW<br>PAY<br>LATER</p>
  <div class="contact">
    <p class="contact__name">OLIVER MARSH</p>
    <p class="contact__role">FOUNDER</p>
    <p class="contact__line">07700 900418</p>
    <p class="contact__line">oliver.marsh_klt</p>
    <p class="contact__line">www.kestrellanefinance.com</p>
    <p class="contact__line contact__email">oliver.marsh@kestrellanefinance.com</p>
  </div>
</section>

</body>
</html>
```